Bottle label design for a mulberry brandy

Please create a label design for a mulberry brandy. The registered brand name is "Kolvat"
The brandy will be produced in Armenia from 100% mulberry.
Color of the product: transparent.
The product will be sold worldwide. The price will be between 30 and 50 USD. So the product will be in premium category.
Therefore we need a solid design, appropriate to the product price category. The design, however, needs to be modern and optimistic.
You can have mulberries on the label or not have, it is up to you.
We have chosen for the product some bottle types, the links to the available bottles you can find in the attachment. Ideally you show a picture of your label on the bottle you selected.

Target Market(s)

worldwide

```html
<!DOCTYPE html>
<html lang="en">
<head>
<meta charset="utf-8">
<title>Kolvat Mulberry Brandy Label</title>
<link rel="stylesheet" href="https://fonts.googleapis.com/css2?family=Montserrat:wght@400;500&display=swap">
<style>
  :root {
    --page: #ffffff;
    --brand-violet: #c77be8;
    --label-lilac: #e8b6fb;
    --label-text: #ffffff;
    --art-top: #7a6478;
    --art-bottom: #5d7a55;
  }
  * { margin: 0; padding: 0; box-sizing: border-box; }
  html, body {
    width: 1200px;
    height: 883px;
    overflow: hidden;
    background: var(--page);
  }
  .label {
    position: relative;
    width: 1200px;
    height: 883px;
    font-family: "Montserrat", Arial, sans-serif;
  }
  .brand-name {
    position: absolute;
    top: 62px;
    left: 0;
    width: 1200px;
    text-align: center;
    font-size: 92px;
    line-height: 1;
    font-weight: 400;
    letter-spacing: 4px;
    color: var(--brand-violet);
    text-transform: uppercase;
  }
  .brand-name .registered {
    font-size: 24px;
    vertical-align: top;
    margin-left: 4px;
    letter-spacing: 0;
  }
  .info-panel {
    position: absolute;
    left: 335px;
    top: 405px;
    width: 530px;
    height: 412px;
    background: var(--label-lilac);
  }
  .fruit-illustration {
    position: absolute;
    left: 490px;
    top: 186px;
    width: 240px;
    height: 404px;
    border-radius: 6px;
    background: linear-gradient(180deg, var(--art-top) 0%, var(--art-bottom) 100%);
  }
  .product-name {
    position: absolute;
    top: 622px;
    left: 0;
    width: 1200px;
    text-align: center;
    font-size: 22px;
    font-weight: 500;
    letter-spacing: 1.5px;
    color: var(--label-text);
  }
  .product-details {
    position: absolute;
    top: 712px;
    left: 362px;
    width: 480px;
    display: flex;
    justify-content: space-between;
    font-family: Arial, Helvetica, sans-serif;
    font-size: 22px;
    color: var(--label-text);
  }
</style>
</head>
<body>
  <main class="label">
    <h1 class="brand-name">Kolvat<span class="registered">®</span></h1>

    <div class="info-panel"></div>

    <div class="fruit-illustration" role="img" aria-label="Illustration of a mulberry branch with ripe dark berries, green leaves and a white blossom"></div>

    <p class="product-name">MULBERRY</p>

    <div class="product-details">
      <span class="composition">100% mulberry</span>
      <span class="volume">Nt Wt. 100mL.</span>
    </div>
  </main>
</body>
</html>
```